SEAFOOD PACKAGING (Products for consumer)

We are looking to create packaging for various seafood products such as octopus and squid. We plan to sell our products in upscale supermarkets.

We are specializing in cut octopus this time.

Please include our company logo. Also, please leave a transparent area so that customers can see the product inside.
Updates

We want to show what is inside, so a picture of the octopus is not required. We need something simple and sophisticated.

Target Market(s)

upscale store in US and ASIA

Industry/Entity Type

Fisheries dealer

Requirements
Must have
• Please include the attached logo,Blue one is preferred.Please leave a transparent part so that the contents of the product can be seen by the consumer.1. product name on packaging →CUT OCTOPUS,TAKO SASHIMI,Highest quality,Top quality etc... 3. What text information should be on the packaging →(It may be edited, but this is the image) The raw materials are caught in a very clean environment and processed in a modern factory with ZEK certification. We are committed to additive-free products. 4. Packing size(cm/inch)→it will be about 19cm*22cm. 5. what kind of packaging do you use →PP or PA 6. dll →ai,jag
Nice to have
• https://quillmora.example/shots/4829174-Velka-Reef We need something simple and sophisticated like this one.
Should not have
• We want to show what is inside, so a picture of the octopus is not required. We need something simple and sophisticated.

```html
<!DOCTYPE html>
<html lang="en">
<head>
<meta charset="utf-8">
<title>Marlo Cut Octopus – Package Front</title>
<link href="https://fonts.googleapis.com/css2?family=Fredoka:wght@600;700&family=Audiowide&family=Montserrat:wght@700;800&display=swap" rel="stylesheet">
<style>
  :root {
    --page: #ffffff;
    --sky: #f2f2f2;
    --sea-top: #1e6cc3;
    --sea-mid: #4ec2f0;
    --sea-low: #1b74cc;
    --wave-line: #17479b;
    --banner: #0a56a4;
    --strip: #1d6ec2;
    --navy-top: #0e4189;
    --navy-low: #07245a;
    --white: #ffffff;
    --title-stroke: #1560b4;
    --badge-green: #6cc33a;
    --window-light: #f4eeea;
    --window-warm: #d9735e;
  }
  * { margin: 0; padding: 0; box-sizing: border-box; }
  html, body {
    width: 1199px;
    height: 1200px;
    overflow: hidden;
    background: var(--page);
  }
  .canvas {
    position: relative;
    width: 1199px;
    height: 1200px;
  }
  .package {
    position: absolute;
    left: 205px;
    top: 133px;
    width: 768px;
    height: 927px;
  }
  .package-art {
    position: absolute;
    inset: 0;
    width: 768px;
    height: 927px;
  }
  .brand-name {
    position: absolute;
    left: 251px;
    width: 267px;
    top: 222px;
    text-align: center;
    font-family: "Montserrat", sans-serif;
    font-weight: 800;
    font-size: 54px;
    letter-spacing: 6px;
    color: var(--white);
  }
  .product-title {
    position: absolute;
    left: 0;
    width: 768px;
    top: 362px;
    text-align: center;
    font-family: "Fredoka", sans-serif;
    font-weight: 700;
    font-size: 86px;
    line-height: 1;
    color: var(--white);
    -webkit-text-stroke: 3px var(--title-stroke);
    paint-order: stroke fill;
    letter-spacing: 1px;
  }
  .product-subtitle {
    position: absolute;
    left: 0;
    width: 768px;
    top: 456px;
    text-align: center;
    font-family: "Audiowide", sans-serif;
    font-size: 36px;
    line-height: 1;
    letter-spacing: 6px;
    color: var(--white);
    -webkit-text-stroke: 2px var(--title-stroke);
    paint-order: stroke fill;
  }
  .net-weight {
    position: absolute;
    left: 289px;
    top: 824px;
    font-family: "Montserrat", sans-serif;
    font-weight: 700;
    font-size: 23px;
    color: var(--white);
    letter-spacing: 0.5px;
  }
</style>
</head>
<body>
<div class="canvas">
  <div class="package">
    <svg class="package-art" viewBox="0 0 768 927" xmlns="http://www.w3.org/2000/svg">
      <defs>
        <linearGradient id="seaGradient" x1="0" y1="0" x2="0" y2="1">
          <stop offset="0" stop-color="var(--sea-top)"/>
          <stop offset="0.45" stop-color="var(--sea-mid)"/>
          <stop offset="1" stop-color="var(--sea-low)"/>
        </linearGradient>
        <linearGradient id="navyGradient" x1="0" y1="0" x2="0" y2="1">
          <stop offset="0" stop-color="var(--navy-top)"/>
          <stop offset="1" stop-color="var(--navy-low)"/>
        </linearGradient>
        <linearGradient id="windowGradient" x1="0" y1="0" x2="1" y2="0.3">
          <stop offset="0" stop-color="var(--window-light)"/>
          <stop offset="0.5" stop-color="var(--window-warm)"/>
          <stop offset="1" stop-color="var(--window-light)"/>
        </linearGradient>
      </defs>

      <rect class="sky" width="768" height="927" fill="var(--sky)"/>

      <path class="sea" fill="url(#seaGradient)"
        d="M0,150 C60,185 130,205 210,190 C260,180 300,170 360,182 C430,196 520,210 600,205 C680,200 730,175 768,158 L768,927 L0,927 Z"/>
      <path class="sea-surface" fill="none" stroke="var(--wave-line)" stroke-width="4"
        d="M0,150 C60,185 130,205 210,190 C260,180 300,170 360,182 C430,196 520,210 600,205 C680,200 730,175 768,158"/>

      <path class="brand-banner" fill="var(--banner)"
        d="M251,0 H518 V328 C470,305 420,300 380,318 C330,340 290,332 251,300 Z"/>
      <circle class="brand-mark" cx="385" cy="150" r="32" fill="none" stroke="var(--white)" stroke-width="8"/>

      <path class="product-window" role="img" aria-label="Clear window showing cut octopus tentacle pieces inside the pack"
        fill="url(#windowGradient)"
        d="M0,640 C200,600 350,560 500,545 C620,532 700,530 768,528 V700 C600,720 400,760 250,790 C150,805 60,806 0,800 Z"/>
      <path class="window-divider" fill="var(--strip)"
        d="M180,808 C300,722 420,600 590,540 L650,533 C490,622 385,722 285,795 Z"/>

      <path class="base-band" fill="url(#navyGradient)"
        d="M0,800 C150,812 300,784 400,762 C550,726 680,692 768,690 V927 H0 Z"/>

      <circle class="additive-free-badge" cx="545" cy="818" r="30" fill="none" stroke="var(--white)" stroke-width="3"/>
      <rect class="certificate-badge" x="606" y="790" width="100" height="56" rx="3" fill="var(--badge-green)"/>
    </svg>

    <div class="brand-name">MARLO</div>
    <h1 class="product-title">CUT OCTOPUS</h1>
    <p class="product-subtitle">TAKO SASHIMI</p>
    <p class="net-weight">Net. Wt. 1.0lb</p>
  </div>
</div>
</body>
</html>
```